Lanterns in Winter

A 3rd Volume of Poetry, dealing with Power, Politics, Love, and General topics. The major theme is the misuse of power across al the continents. I would like a background map of the world and a stylistic fire depicting symbolically each continent on fire. This can be abstract. The title may be included in the artwork. alone or in conjunction with the world map.

```html
<!DOCTYPE html>
<html lang="en">
<head>
<meta charset="utf-8">
<title>Lanterns in Winter — Poetry Volume III</title>
<link rel="stylesheet" href="https://fonts.googleapis.com/css2?family=Courgette&family=Tinos&display=swap">
<style>
  :root {
    --ink: #000000;
    --title-red: #e0202a;
    --author-white: #ffffff;
    --volume-gold: #f2b418;
    --fire-deep: #c8260f;
    --fire-mid: #ee6a12;
    --fire-light: #f7b32e;
  }
  * { margin: 0; padding: 0; box-sizing: border-box; }
  html, body {
    width: 796px;
    height: 1200px;
    overflow: hidden;
    background: var(--ink);
  }
  .cover {
    position: relative;
    width: 796px;
    height: 1200px;
    background: var(--ink);
    overflow: hidden;
  }
  .cover__artwork {
    position: absolute;
    top: 262px;
    left: -20px;
    width: 836px;
    height: 720px;
    background: linear-gradient(100deg,
      var(--fire-light) 0%,
      var(--fire-mid) 30%,
      var(--fire-deep) 55%,
      var(--fire-mid) 80%,
      var(--fire-deep) 100%);
    -webkit-mask-image: radial-gradient(ellipse 50% 50% at 50% 50%, #000 55%, transparent 100%);
    mask-image: radial-gradient(ellipse 50% 50% at 50% 50%, #000 55%, transparent 100%);
  }
  .cover__title {
    position: absolute;
    top: 76px;
    left: 0;
    width: 100%;
    text-align: center;
    font-family: "Courgette", cursive;
    font-weight: 400;
    font-size: 78px;
    line-height: 1;
    color: var(--title-red);
  }
  .cover__author {
    position: absolute;
    top: 172px;
    left: 0;
    width: 100%;
    text-align: center;
    font-family: "Tinos", "Times New Roman", serif;
    font-size: 58px;
    line-height: 1;
    color: var(--author-white);
  }
  .cover__volume {
    position: absolute;
    top: 1072px;
    left: 0;
    width: 100%;
    text-align: center;
    font-family: "Tinos", "Times New Roman", serif;
    font-size: 47px;
    line-height: 1;
    color: var(--volume-gold);
  }
</style>
</head>
<body>
  <main class="cover">
    <div class="cover__artwork" role="img" aria-label="World map with every continent rendered in swirling orange, red and yellow flames on black"></div>
    <h1 class="cover__title">Lanterns in Winter</h1>
    <p class="cover__author">Dorian K Hale</p>
    <p class="cover__volume">Poetry Volume III</p>
  </main>
</body>
</html>
```